Funeral Services Site

We need a website for a Funeral Services company. The old website is: www.rouwcentrumdelvoort.be We need the same structure and text.

Target Market(s)

Customers.

Coding

Coded - Design and coding required

Number of Pages Required

4 page

Font styles to use
Serif
Sans Serif
Script

```html
<!DOCTYPE html>
<html lang="en">
<head>
<meta charset="utf-8">
<title>Funeral home Delvoort</title>
<link href="https://fonts.googleapis.com/css2?family=Playfair+Display:wght@400;700&family=Open+Sans:wght@400;600;700&family=Dancing+Script:wght@600&display=swap" rel="stylesheet">
<style>
:root{
  --ink:#222;
  --muted:#666;
  --light:#f0f0f0;
  --line:#d6d6d6;
  --accent:#f07c1e;
  --dark:#1c1c1c;
  --white:#fff;
  --frame:#c9c9c9;
}
*{box-sizing:border-box;margin:0;padding:0}
html,body{width:1200px;height:3644px;overflow:hidden}
body{font-family:"Open Sans",Arial,sans-serif;color:var(--ink);background:var(--white);position:relative;font-size:13px;line-height:1.6}
.serif{font-family:"Playfair Display",Georgia,serif}
section,header,footer{position:absolute;left:0;width:1200px}
.abs{position:absolute}
.fill{display:block}

/* header */
.site-header{top:0;height:64px;background:var(--white)}
.brand{left:40px;top:10px;display:flex;align-items:center;gap:10px}
.brand-mark{width:14px;height:14px;background:var(--ink)}
.brand-name{font-family:"Playfair Display",Georgia,serif;font-weight:700;font-size:20px;line-height:1.1;width:160px}
.nav{right:50px;top:20px;display:flex;gap:40px;align-items:center;font-size:13px}
.nav .login{border:1px solid var(--ink);padding:2px 14px}

/* hero */
.hero{top:64px;height:470px;background:linear-gradient(180deg,#55624a 0%,#3b3f33 45%,#2a2b25 100%)}
.hero-title{top:130px;width:100%;text-align:center;color:var(--white);font-family:"Playfair Display",Georgia,serif;font-weight:700;font-size:40px;line-height:1.3}
.hero-title span{display:block}
.btn{display:inline-block;font-size:20px;padding:8px 22px;letter-spacing:.5px}
.btn-light{background:var(--white);color:var(--ink)}
.btn-ghost{border:2px solid var(--white);color:var(--white)}
.hero-actions{top:300px;width:100%;display:flex;justify-content:center;gap:18px}
.dots{right:36px;top:262px;display:flex;flex-direction:column;gap:10px}
.dots i{width:9px;height:9px;border-radius:50%;background:rgba(255,255,255,.55)}
.dots i:first-child{background:var(--white)}

/* sections common */
.section-title{width:100%;text-align:center;font-family:"Playfair Display",Georgia,serif;font-size:40px;letter-spacing:1px}
.section-sub{width:100%;text-align:center;font-size:12px;color:var(--muted)}

/* condole */
.condole{top:534px;height:630px}
.condole .section-title{top:90px}
.condole .section-sub{top:146px}
.card{top:190px;width:296px;height:170px;border:1px solid var(--line);padding:14px;display:flex;gap:12px;font-size:10px;color:var(--muted);line-height:1.5}
.card .portrait{width:64px;height:76px;flex:none;background:linear-gradient(#bdbdbd,#8a8a8a)}
.card .name{font-family:"Dancing Script",cursive;font-size:22px;color:var(--ink);line-height:1.1}
.card .date{color:var(--accent);font-size:10px;margin-bottom:4px}
.card b{color:var(--ink)}
.btn-dark{top:530px;left:530px;width:140px;height:54px;background:var(--dark);color:var(--white);text-align:center;line-height:54px;font-weight:700;font-size:13px}

/* about */
.about{top:1164px;height:380px;background:var(--light)}
.about-photo{left:40px;top:40px;width:360px;height:300px;background:linear-gradient(180deg,#c7d6e0 0%,#9bb08a 55%,#6d8050 100%);box-shadow:-10px 0 0 var(--white)}
.about-text{left:460px;top:50px;width:520px}
.about-text h2{font-family:"Playfair Display",Georgia,serif;font-size:40px;font-weight:400;line-height:1.1}
.about-text .lead{font-size:17px;margin:8px 0 14px;line-height:1.4}
.about-text p{font-size:11px;color:var(--muted)}
.about-text .more{margin-top:10px;font-weight:700;color:var(--ink);font-size:12px}

/* organisation */
.organisation{top:1544px;height:740px}
.org-text{left:96px;top:190px;width:430px;font-size:11px;color:var(--muted)}
.org-text h2{font-family:"Playfair Display",Georgia,serif;font-size:30px;color:var(--ink);font-weight:400;line-height:1.25;margin-bottom:14px}
.org-text p{margin-bottom:10px}
.frame{border:16px solid var(--frame)}
.frame-a{left:620px;top:120px;width:250px;height:240px}
.photo-a{left:660px;top:80px;width:240px;height:250px;background:linear-gradient(160deg,#6e7a4f,#3e4a2c 60%,#2c3521)}
.frame-b{left:760px;top:320px;width:220px;height:330px}
.photo-b{left:800px;top:330px;width:200px;height:300px;background:linear-gradient(180deg,#b8c7d6 0%,#8a9a73 40%,#5a7040 100%)}

/* cta */
.cta{top:2284px;height:316px;background:linear-gradient(180deg,#2c2a26,#3f3a2c 60%,#1e1c18)}
.cta-text{top:90px;width:100%;text-align:center;color:var(--white);font-size:28px;line-height:1.35;text-transform:uppercase}
.cta-actions{top:206px;width:100%;display:flex;justify-content:center;gap:14px}
.cta-actions .btn{font-size:16px;padding:6px 22px;border:2px solid var(--white)}

/* news */
.news{top:2600px;height:540px}
.news .section-title{top:50px;text-transform:none}
.news .section-sub{top:108px}
.post{top:150px;width:290px}
.post .thumb{width:290px;height:190px}
.post .meta{margin:-22px 0 0 24px;width:188px;height:28px;background:var(--accent);color:var(--white);font-size:9px;display:flex;align-items:center;justify-content:space-around;position:relative}
.post h3{font-size:16px;font-weight:700;text-align:center;margin-top:16px}
.post p{font-size:10px;color:var(--muted);text-align:center;line-height:1.5;padding:0 14px}

/* footer */
.site-footer{top:3140px;height:504px;background:var(--white);border-top:1px solid var(--line)}
.foot-col{top:50px;font-size:11px;color:var(--muted)}
.foot-col h4{font-size:13px;color:var(--ink);font-weight:700;margin-bottom:12px;letter-spacing:.5px}
.foot-col li{list-style:none;margin-bottom:6px}
.foot-brand .brand-name{font-size:20px;color:var(--ink);margin-bottom:10px}
.social{display:flex;gap:6px;margin-top:12px}
.social i{width:22px;height:22px;border-radius:50%;background:var(--ink)}
.contact-row{display:flex;gap:8px;margin-bottom:10px}
.contact-row svg{flex:none;margin-top:2px}
.gallery{display:grid;grid-template-columns:repeat(2,110px);gap:8px}
.gallery span{height:70px;display:block}
.bottom-bar{left:0;bottom:0;width:1200px;height:56px;background:var(--dark);color:#bbb;font-size:11px;text-align:center;line-height:56px}
</style>
</head>
<body>

<header class="site-header">
  <div class="brand abs"><span class="brand-mark"></span><span class="brand-name">Funeral home Delvoort</span></div>
  <nav class="nav abs"><span>Home</span><span>About us</span><span>Condole online</span><span>Order flowers</span><span>Contact</span><span class="login">Login</span></nav>
</header>

<section class="hero" role="img" aria-label="Photograph of a wooden coffin with white flowers">
  <h1 class="hero-title abs"><span>Funeral home Delvoort bvba:</span><span>a personal service in farewell guidance</span></h1>
  <div class="hero-actions abs"><span class="btn btn-light">012 34 56 78</span><span class="btn btn-ghost">CONTACT US</span></div>
  <div class="dots abs"><i></i><i></i><i></i></div>
</section>

<section class="condole">
  <h2 class="section-title abs">CONDOLE ONLINE</h2>
  <p class="section-sub abs">Do you want to leave a message for the family of a deceased person?</p>
  <article class="card abs" style="left:96px">
    <div class="portrait" role="img" aria-label="Portrait of the deceased"></div>
    <div><div class="name">Maria Claes</div><div class="date">March 14, 1940 – May 4, 2019</div>We remember a warm and caring mother who loved her garden. Leave a few words for the family. <b>READ MORE</b></div>
  </article>
  <article class="card abs" style="left:452px">
    <div class="portrait" role="img" aria-label="Portrait of the deceased"></div>
    <div><div class="name">Louis Peeters</div><div class="date">June 2, 1936 – April 27, 2019</div>A kind husband and grandfather, always ready to help others. Share a memory with his loved ones. <b>READ MORE</b></div>
  </article>
  <article class="card abs" style="left:808px">
    <div class="portrait" role="img" aria-label="Portrait of the deceased"></div>
    <div><div class="name">Jan Willems</div><div class="date">Sept 18, 1945 – April 25, 2019</div>A gentle man who loved music and long walks. Write a message of comfort for the family. <b>READ MORE</b></div>
  </article>
  <div class="btn-dark abs">VIEW ALL</div>
</section>

<section class="about">
  <div class="about-photo abs" role="img" aria-label="Photograph of the funeral home building with a large tree"></div>
  <div class="about-text abs">
    <h2>ABOUT US</h2>
    <p class="lead">Mourning center Delvoort, a complete service in mourning and farewell guidance</p>
    <p>Saying goodbye to a loved one is one of the toughest things in a lifetime. Funeral home Delvoort is there to take care of all the practical and administrative matters involved, so you can say goodbye in peace. Our people have a lot of experience in farewell guidance and stand by you day and night with calm, clear and personal support at every step.</p>
    <p class="more">Read more »</p>
  </div>
</section>

<section class="organisation">
  <div class="org-text abs">
    <h2>Organization funeral and worship</h2>
    <p>The organization of the funeral ceremony is a moment of reflection, where the personality of the deceased can be beautifully highlighted. Our team will assist you in this and select the most fitting music, texts and photos with you in order to create a worthy farewell.</p>
    <p>The funeral can take place in your parish church or in our auditorium, which can accommodate a maximum of 150 guests. We can arrange the following for you:</p>
    <p>– vigil the night before the funeral</p>
    <p>– prayer service with priest (if possible)</p>
    <p>– eucharistic celebration with priest (on Tuesday and Friday in the parish of choice)</p>
  </div>
  <div class="frame frame-a abs"></div>
  <div class="photo-a abs" role="img" aria-label="Photograph of a woman laying white flowers at a grave"></div>
  <div class="frame frame-b abs"></div>
  <div class="photo-b abs" role="img" aria-label="Photograph of a cemetery with rows of white crosses"></div>
</section>

<section class="cta" role="img" aria-label="Photograph of lit candles in the evening">
  <p class="cta-text abs">Do you have any questions or would you like to<br>call in our funeral home? Contact us. We are here<br>for you.</p>
  <div class="cta-actions abs"><span class="btn btn-light">012 34 56 78</span><span class="btn btn-ghost">CONTACT US</span></div>
</section>

<section class="news">
  <h2 class="section-title abs">Funeral Latest News</h2>
  <p class="section-sub abs">Lorem ipsum is simply dummy text of the printing and typesetting</p>
  <article class="post abs" style="left:96px">
    <div class="thumb" role="img" aria-label="Photograph of candles and white flowers" style="background:linear-gradient(160deg,#e8e0d0,#9c8f78)"></div>
    <div class="meta"><span>MAY 6 2019</span><span>BY ADMIN</span></div>
    <h3>Contrary to popular belief</h3>
    <p>Lorem ipsum is simply dummy text of the printing and typesetting industry. Lorem ipsum has been the industry standard dummy text ever since the 1500s.</p>
  </article>
  <article class="post abs" style="left:455px">
    <div class="thumb" role="img" aria-label="Photograph of mourners holding pink flowers" style="background:linear-gradient(160deg,#9aa58a,#3a3a33)"></div>
    <div class="meta"><span>MAY 6 2019</span><span>BY ADMIN</span></div>
    <h3>Contrary to popular belief</h3>
    <p>Lorem ipsum is simply dummy text of the printing and typesetting industry. Lorem ipsum has been the industry standard dummy text ever since the 1500s.</p>
  </article>
  <article class="post abs" style="left:814px">
    <div class="thumb" role="img" aria-label="Photograph of a red wooden coffin with flowers" style="background:linear-gradient(160deg,#c69a7a,#7a3a22)"></div>
    <div class="meta"><span>MAY 6 2019</span><span>BY ADMIN</span></div>
    <h3>Contrary to popular belief</h3>
    <p>Lorem ipsum is simply dummy text of the printing and typesetting industry. Lorem ipsum has been the industry standard dummy text ever since the 1500s.</p>
  </article>
</section>

<footer class="site-footer">
  <div class="foot-col foot-brand abs" style="left:96px;width:240px">
    <div class="brand-name">Funeral home Delvoort</div>
    <p>Funeral home Delvoort is a family business from Hoeveldorp. Call us for farewell guidance, day and night, with care and respect.</p>
    <div class="social"><i></i><i></i><i></i><i></i></div>
  </div>
  <div class="foot-col abs" style="left:440px">
    <h4>QUICK LINKS</h4>
    <ul><li>› Home</li><li>› About us</li><li>› Condole online</li><li>› Order flowers</li><li>› Contact</li></ul>
  </div>
  <div class="foot-col abs" style="left:630px;width:220px">
    <h4>CONTACT US</h4>
    <div class="contact-row"><svg width="12" height="14" viewBox="0 0 12 14"><path d="M6 0a5 5 0 0 0-5 5c0 4 5 9 5 9s5-5 5-9a5 5 0 0 0-5-5zm0 7a2 2 0 1 1 0-4 2 2 0 0 1 0 4z" fill="#222"/></svg><span>Lindenlaan 12<br>3700 Hoeveldorp</span></div>
    <div class="contact-row"><svg width="12" height="12" viewBox="0 0 12 12"><path d="M2.5 0l2 3-1.2 1.4a7 7 0 0 0 4.3 4.3L9 7.5l3 2-1 2.5C5 12 0 7 0 1z" fill="#222"/></svg><span>Tel: 012 34 56 78<br>Fax: 012 34 56 79</span></div>
    <div class="contact-row"><svg width="12" height="10" viewBox="0 0 12 10"><rect x=".5" y=".5" width="11" height="9" fill="none" stroke="#222"/><path d="M.5.5L6 5l5.5-4.5" fill="none" stroke="#222"/></svg><span>info@rouwcentrumdelvoort.be</span></div>
  </div>
  <div class="foot-col abs" style="left:900px">
    <h4>PHOTO GALLERY</h4>
    <div class="gallery">
      <span role="img" aria-label="Photograph of a floral arrangement" style="background:#8a7a5e"></span>
      <span role="img" aria-label="Photograph of a coffin" style="background:#6b4a33"></span>
      <span role="img" aria-label="Photograph of the auditorium" style="background:#9a9384"></span>
      <span role="img" aria-label="Photograph of candles" style="background:#5c4f3a"></span>
      <span role="img" aria-label="Photograph of the garden" style="background:#6d7a55"></span>
      <span role="img" aria-label="Photograph of white flowers" style="background:#c9c3b5"></span>
    </div>
  </div>
  <div class="bottom-bar abs">©2019 Studio Nova · Sitemap · Privacy Policy</div>
</footer>

</body>
</html>
```